Photographer's price list

I am a photographer who runs a studio (Pinefield Studio) and need to have a document to send clients detailing my packages (collections) and prices. I have written the text in a word document and need a designer to lay it out for me using my logo and two specific fonts: DejaVu Sans and LainieDaySH.

The look should be clean and modern and keep in the same style as my logo. I will primarily be using the final product as a PDF file to email to potential clients. It should stay black and white.

I would also like to be able to update the text myself as my prices and packages change. So I would like a PSD file.

I think I would like for the document to be in landscape format with "Collections" on one side and A la Carte on the other, but I am open to other ideas.

As for sizing, it should be a standard size so that clients can print it out if they like.

Requirements
Must have
• my logo
fonts: DejaVu and LainieDaySH
Easy to email
Easy to display on one page upon opening
Standard size so that printing from a home computer is easy to do.

```html
<!DOCTYPE html>
<html lang="en">
<head>
<meta charset="utf-8">
<title>Pinefield Studio – 2013 Photography Collections</title>
<link rel="stylesheet" href="https://fonts.googleapis.com/css2?family=Noto+Sans:ital,wght@0,400;0,700;1,400&family=Sacramento&display=swap">
<style>
  :root{
    --backdrop:#c9c9c9;
    --page:#ffffff;
    --page-grey:#e4e4e4;
    --panel-grey:#d8d8d8;
    --ink:#1e1e1e;
    --ink-soft:#6f6f6f;
    --ink-faint:#9a9a9a;
    --tag:#262626;
    --photo-light:#d6d6d6;
    --photo-mid:#9e9e9e;
    --photo-dark:#4a4a4a;
  }
  *{box-sizing:border-box;margin:0;padding:0}
  html,body{width:1200px;height:851px;overflow:hidden}
  body{background:var(--backdrop);font-family:"Noto Sans",sans-serif;color:var(--ink);position:relative}
  .spread{position:absolute;top:222px;width:585px;height:407px;background:var(--page);box-shadow:0 2px 8px rgba(0,0,0,.25);overflow:hidden}
  .spread--outside{left:10px}
  .spread--inside{left:605px}
  .page{position:absolute;top:0;height:100%}
  .script{font-family:"Sacramento",cursive;font-weight:400}

  /* a la carte page */
  .alacarte{left:0;width:292px;background:var(--page-grey);padding:9px 12px 0 12px}
  .alacarte__title{font-size:19px;line-height:20px}
  .alacarte__intro{font-size:6.2px;line-height:8.2px;margin:1px 0 2px}
  .item__label{font-family:"Sacramento",cursive;font-size:12px;line-height:14px;height:14px}
  .item__box{display:flex;background:var(--page);margin-bottom:3px;min-height:34px;align-items:stretch}
  .item__box--tall{min-height:52px}
  .price-tag{background:var(--tag);color:#fff;width:14px;flex:none;writing-mode:vertical-rl;transform:rotate(180deg);font-family:"Sacramento",cursive;font-size:10px;text-align:center;margin:4px 6px 4px 4px;line-height:14px;white-space:nowrap;overflow:hidden}
  .item__text{font-size:6.2px;line-height:8.2px;padding:4px 6px 4px 0;align-self:center}
  .item__text b{font-weight:700}
  .item__note{color:var(--ink-faint)}

  /* cover page */
  .cover{left:292px;width:293px;background:var(--page)}
  .photo{position:absolute}
  .cover__title{position:absolute;left:12px;top:158px;text-align:center;font-size:32px;line-height:30px;width:135px}
  .cover__title span{display:block;font-size:21px;line-height:21px}

  /* studio name */
  .studio-name{position:absolute;font-size:9px;letter-spacing:1px;text-transform:uppercase;white-space:nowrap;text-align:center;color:var(--ink)}

  /* inside left */
  .includes{left:0;width:292px;background:var(--page)}
  .includes__heading{position:absolute;left:152px;top:198px;font-size:16px;line-height:18px}
  .includes__copy{position:absolute;left:152px;top:222px;width:128px;font-size:5.6px;line-height:8px;color:var(--ink-soft)}
  .includes__copy p{margin-bottom:6px}

  /* collections page */
  .collections{left:292px;width:293px;background:linear-gradient(90deg,#e6e6e6,var(--panel-grey))}
  .collection{position:absolute;left:20px;width:262px;height:62px}
  .collection__stack{position:absolute;left:0;top:6px;width:56px;height:44px}
  .collection__stack i{position:absolute;inset:0;background:#f4f4f4;border:1px solid #bbb}
  .collection__stack i:nth-child(1){transform:rotate(-6deg)}
  .collection__stack i:nth-child(2){transform:rotate(4deg)}
  .collection__stack .photo{inset:3px;border:0}
  .collection .price-tag{position:absolute;left:52px;top:4px;height:46px;margin:0;width:15px;font-size:12px;line-height:15px}
  .collection__body{position:absolute;left:78px;top:0;width:184px}
  .collection__name{font-family:"Sacramento",cursive;font-size:15px;line-height:17px}
  .collection__text{font-size:5.8px;line-height:7.6px}
  .collection__note{font-size:5.6px;line-height:7.4px;color:var(--ink-faint);font-style:italic;margin-top:4px}
</style>
</head>
<body>

<section class="spread spread--outside">
  <div class="page alacarte">
    <h2 class="alacarte__title script">a la carte pricing</h2>
    <p class="alacarte__intro">These products may be purchased separately to complement your collection. A consultation with Mara will help you decide which products are best for gifts and for your home.</p>

    <div class="item">
      <div class="item__label">high resolution digital images</div>
      <div class="item__box"><div class="price-tag">25€</div><p class="item__text">Perfect if you just need to add "one more image" to your collection! High-resolution jpeg file.</p></div>
    </div>
    <div class="item">
      <div class="item__label">matt prints</div>
      <div class="item__box"><div class="price-tag">25€</div><p class="item__text"><b>20x30 cm and smaller.</b> Each print is professionally edited, printed on archival photo paper. <span class="item__note">Purchase includes the JPEG file for your personal digital use</span></p></div>
    </div>
    <div class="item">
      <div class="item__label">verrano prints</div>
      <div class="item__box"><div class="price-tag">45€</div><p class="item__text"><b>30x40 cm.</b> Prints on Verrano (watercolor) paper are Mara's favorite for large format color prints.</p></div>
    </div>
    <div class="item">
      <div class="item__label">canvas prints</div>
      <div class="item__box"><div class="price-tag">100€</div><p class="item__text"><b>30x40 cm.</b> Ready-to-hang, stretched canvas wall art of your favorite images.</p></div>
    </div>
    <div class="item">
      <div class="item__label">framed + matted prints</div>
      <div class="item__box"><div class="price-tag">350€</div><p class="item__text"><b>30x40 inch.</b> Beautiful Verrano prints finished with wide mats and simple, elegant frames of your choice</p></div>
    </div>
    <div class="item">
      <div class="item__label">custom designed albums</div>
      <div class="item__box item__box--tall"><div class="price-tag">100€+</div><p class="item__text">Images from your session are selected for the custom design of an album and bound in a book for a modern presentation of your images. There are a number of cover choices for the classic flush-mount and beautifully crafted albums.<br><b><i>A great way to display all of your favorite images from your session on your coffee table.</i></b></p></div>
    </div>
  </div>

  <div class="page cover">
    <div class="photo" role="img" aria-label="Black and white family portrait on a bed" style="left:0;top:0;width:180px;height:132px;background:linear-gradient(160deg,var(--photo-light),var(--photo-mid) 60%,#eee)"></div>
    <div class="photo" role="img" aria-label="Black and white portrait of a mother holding a newborn" style="left:183px;top:0;width:110px;height:132px;background:linear-gradient(200deg,#eaeaea,var(--photo-mid))"></div>
    <h1 class="cover__title script">2013<span>photography</span><span>collections</span></h1>
    <div class="studio-name" style="left:150px;top:183px;width:120px">Pinefield Studio</div>
    <div class="photo" role="img" aria-label="Black and white portrait of a young girl" style="left:0;top:270px;width:56px;height:137px;background:linear-gradient(180deg,#e0e0e0,var(--photo-mid))"></div>
    <div class="photo" role="img" aria-label="Black and white portrait of a baby" style="left:58px;top:270px;width:56px;height:137px;background:linear-gradient(180deg,#d0d0d0,#8a8a8a)"></div>
    <div class="photo" role="img" aria-label="Black and white portrait of a father and child" style="left:116px;top:270px;width:56px;height:137px;background:linear-gradient(180deg,#b5b5b5,var(--photo-dark))"></div>
    <div class="photo" role="img" aria-label="Black and white close portrait of an infant" style="left:174px;top:270px;width:60px;height:137px;background:linear-gradient(180deg,#c8c8c8,#7d7d7d)"></div>
    <div class="photo" role="img" aria-label="Black and white portrait of a toddler" style="left:236px;top:270px;width:57px;height:137px;background:linear-gradient(180deg,#e5e5e5,#a5a5a5)"></div>
  </div>
</section>

<section class="spread spread--inside">
  <div class="page includes">
    <div class="photo" role="img" aria-label="Collage of black and white family and newborn portraits" style="left:0;top:0;width:136px;height:407px;background:linear-gradient(180deg,#cfcfcf,#8f8f8f 30%,#e2e2e2 50%,#9a9a9a 75%,var(--photo-dark))"></div>
    <div class="studio-name" style="left:150px;top:96px;width:130px">Pinefield Studio</div>
    <h3 class="includes__heading script">All collections include:</h3>
    <div class="includes__copy">
      <p>One to two hour portrait session with photographer in location of your choice (unlimited time if necessary!)</p>
      <p>Mara will create a presentation video with hand-selected music and custom editing, which tells your story, highlights the best images, and reveals the connections within your family.</p>
      <p>An online gallery for viewing and ordering helps you share your images with family and friends.</p>
    </div>
  </div>

  <div class="page collections">
    <div class="collection" style="top:40px">
      <div class="collection__stack"><i></i><i></i><div class="photo" role="img" aria-label="Black and white photo of a sleeping baby" style="background:linear-gradient(135deg,#ddd,#8c8c8c)"></div></div>
      <div class="price-tag">300€</div>
      <div class="collection__body">
        <div class="collection__name">Collection 1</div>
        <p class="collection__text">Your favorite <b>five</b> images from the session will be professionally edited and presented to you on disk as high resolution jpegs</p>
      </div>
    </div>
    <div class="collection" style="top:128px">
      <div class="collection__stack"><i></i><i></i><div class="photo" role="img" aria-label="Black and white photo of a baby" style="background:linear-gradient(135deg,#e0e0e0,#9a9a9a)"></div></div>
      <div class="price-tag">400€</div>
      <div class="collection__body">
        <div class="collection__name">Collection 2</div>
        <p class="collection__text">Your favorite <b>ten</b> images from the session will be professionally edited and given to you on disk as high resolution jpegs.</p>
        <p class="collection__note">Your favorite two images from the session will be professionally printed for you (20x30cm) on Verrano paper, Mara's favorite for portraits</p>
      </div>
    </div>
    <div class="collection" style="top:216px">
      <div class="collection__stack"><i></i><i></i><div class="photo" role="img" aria-label="Black and white family portrait" style="background:linear-gradient(135deg,#bdbdbd,var(--photo-dark))"></div></div>
      <div class="price-tag">500€</div>
      <div class="collection__body">
        <div class="collection__name">Collection 3</div>
        <p class="collection__text">Your favorite <b>fifteen</b> images from the session will be professionally edited and presented to you on disk as high resolution jpegs</p>
        <p class="collection__note">Your favorite two images from the session will be professionally printed for you (20x30cm) on Verrano paper, Mara's favorite for portraits</p>
      </div>
    </div>
    <div class="collection" style="top:304px">
      <div class="collection__stack"><i></i><i></i><div class="photo" role="img" aria-label="Black and white photo of a newborn" style="background:linear-gradient(135deg,#e4e4e4,#a0a0a0)"></div></div>
      <div class="price-tag">600€</div>
      <div class="collection__body">
        <div class="collection__name">Collection 4</div>
        <p class="collection__text"><b>ALL</b> presented images from the session will be professionally edited and presented to you on disk as high resolution jpegs (approx 40+ images)</p>
        <p class="collection__note">Your favorite two images from the session will be professionally printed for you (20x30cm) on Verrano paper, Mara's favorite for portraits</p>
      </div>
    </div>
  </div>
</section>

</body>
</html>
```